依頼詳細
<現状サイトの課題>
①一目で、何をしている会社なのかが分からない。
⇒商品画像・作業画像などを入れ、分かりやすく目を引き付けるようにする。

②項目が小さく、引き付けにくいデザイン。
⇒アイコンを大きくして、デザイン性を持たせる。

③自社の強みを視覚化できていない。
⇒図や写真を追加し、視覚的に伝わるようにする。

④自社の新着情報がないので社内の動きが把握できない。
⇒新着ニュースを追加し社内の動きが把握できるようにする。

⑤企業規模が小さく感じてしまう。
⇒洗練されたデザイン、コンテンツの充実、グローバルサイトの作成により企業規模をワンランク大きく見えるように表現する。
----------------------------------
<現在のサイト>
明確なサイトの情報共有はできませんが、TOPページの情報を一部伏せて共有します。添付の”TOPページ”をご参照ください。

<サイトリニューアルの方針>
①強みを明確にする為、全体的に画像化し打ち出したい。TOPページは動画を掲載し、よりリアルにユーザー様にイメージが伝わるデザインにする。

②企業規模をワンランク大きく見えるように表現し、グローバル化についてもアピールすることで、事業規模の大きい信頼出来る会社であることが分かるようにし、新規顧客の獲得および定着するようにサイトリニューアルを行う。

③必須機能
・TOPページへ動画を埋め込む。
・スマホ対応(レスポンシブウェブデザイン)にする。
・ウェブ見積り機能を設け、いつでも見積りが確認できるようにする。(TOPページにバナーを設けるなどデザインする)

<イメージ参考サイト>
①メインカラーをブルーとし、TOPページを開くとすぐに大きな画像イメージが見えます。
https://www.e-hariwa.co.jp/

②トップページに表示される、動画イメージです。
https://www.dovel.co.jp/

③コンテンツの配置や施工事例が見やすいです。
http://www.tasemi-kk.com/

④TOPページに施工写真や文字が挿入されており分かりやすい。また企業イメージがよく考えられており、ブランディングされています。
http://www.fujiyaga.co.jp/

<カラーテーマ>
①青系(堅実・信頼・クール)または水色系(さわやか・清潔感)

②青4割、白6割の配色のイメージでお願いします。制作の際は、カラーチャート(カラーを選んだ理由)もご提示いただけると幸いです。

<重視する点/検討基準>
①サイトコンセプトにあったデザイン(ご提案の際は、制作頂いたデザインコンセプト及びデザイン説明コメントの記載をお願い致します)

②納期厳守

<具体的な制作数>
TOPページ:1ページ(PC版のデザイン制作をお願いします)

<選考の進め方>
ご提案頂いたデザイン内容・コンセプトなどをもとに、プロジェクトメンバーで選考、決定致します。
※今回は、トップページデザインのみの見積りとなります。
今後、コーディングを依頼する可能性もございます。その場合は改めてクリエタスを通じてご依頼させて頂きます。パララックスデザインでのコーディングも条件として入れてまいります。
1ページ
青系、水色系
• イラストレーター形式 (.ai)
• フォトショップ形式 (.psd)
追記です。
サイトコンセプトの資料も添付いたします。
宜しくお願いいたします。

クライアント様と協議させていただき、コンセプトに合った総合的なデザインを評価させて頂きました。
その中で、クライアント様からの評価が多かった「Pixfern様」を当選とさせていただきました。ありがとうございました。

ランサーの皆さん、このように沢山の素敵なデザインをご提案頂き本当にありがとうございました。
コンセプトを基に、クライアント様とも大いに悩んで決定させて頂きました。
また、選定が期限間近になってしまいましたこと、申し訳ございませんでした。

機会があれば、今後ともどうぞ宜しくお願い致します。

```html
<!DOCTYPE html>
<html lang="ja">
<head>
<meta charset="utf-8">
<title>SORAMICHI KOGYO</title>
<link href="https://fonts.googleapis.com/css2?family=Noto+Sans+JP:wght@400;500;700&family=Noto+Serif+JP:wght@400;600&display=swap" rel="stylesheet">
<style>
:root{
  --blue:#1560b5;
  --blue-deep:#0d4a93;
  --blue-light:#5aa6e0;
  --sky:#cfe6f6;
  --ink:#333;
  --muted:#888;
  --line:#d8d8d8;
  --gray-bg:#efefef;
  --dark:#3a3a3a;
  --gold:#c9a43a;
  --orange:#e06a1e;
  --white:#fff;
}
*{box-sizing:border-box;margin:0;padding:0}
html,body{width:1200px;height:2760px;overflow:hidden}
body{font-family:"Noto Sans JP",sans-serif;color:var(--ink);background:var(--white);position:relative;font-size:13px}
.serif{font-family:"Noto Serif JP",serif}
.abs{position:absolute}
.ph{position:absolute}

/* header */
.topbar{top:0;left:0;width:1200px;height:48px;background:var(--white)}
.brand{font-family:"Noto Sans JP",sans-serif;font-weight:700;color:var(--blue-deep);letter-spacing:2px;white-space:nowrap}
.topbar .brand{position:absolute;left:0;width:1200px;text-align:center;top:13px;font-size:17px}
.topbar .home-ico{position:absolute;left:150px;top:14px;width:20px;height:20px}
.topbar .tools{position:absolute;right:140px;top:15px;display:flex;gap:10px;color:var(--muted);font-size:12px}
.nav{top:48px;left:0;width:1200px;height:60px;background:var(--blue);display:flex;justify-content:center}
.nav a{width:120px;height:60px;display:flex;flex-direction:column;align-items:center;justify-content:center;color:var(--white);text-decoration:none;font-size:12px;border-right:1px solid rgba(255,255,255,.25)}
.nav a small{font-size:9px;opacity:.75;margin-top:2px}
.nav a.current{background:var(--white);color:var(--blue)}

/* hero */
.hero{top:108px;left:0;width:1200px;height:452px;background:linear-gradient(180deg,#9ec9ec 0%,#d9ecf8 45%,#f3f8fc 100%);overflow:hidden}
.hero .visual{left:0;top:0;width:1200px;height:452px;background:radial-gradient(ellipse at 68% 45%,rgba(21,96,181,.55),rgba(21,96,181,0) 55%),linear-gradient(160deg,rgba(255,255,255,0) 40%,rgba(255,255,255,.7) 85%)}
.hero .copy{left:0;width:1200px;top:150px;text-align:center;color:var(--white);text-shadow:0 1px 6px rgba(0,40,90,.35)}
.hero .copy p{font-size:24px;letter-spacing:6px}
.hero .copy h1{font-size:40px;font-weight:400;letter-spacing:4px;margin-top:6px}

/* section titles */
.sec-title{left:0;width:1200px;text-align:center}
.sec-title h2{display:inline-flex;align-items:center;gap:18px;font-family:"Noto Serif JP",serif;font-weight:400;font-size:26px;letter-spacing:4px;color:var(--ink)}
.sec-title h2::before,.sec-title h2::after{content:"";width:40px;height:1px;background:var(--ink)}
.sec-title p{font-size:10px;color:var(--muted);margin-top:2px}

/* about */
.about-sky{left:0;top:760px;width:600px;height:290px;background:linear-gradient(180deg,rgba(255,255,255,1) 0%,#cfe3f4 55%,#a9cdee 100%)}
.about-swoosh{left:600px;top:560px;width:600px;height:480px;background:linear-gradient(135deg,#f7fbfe 0%,#e2eff9 100%)}
.about-box{left:150px;top:680px;width:360px}
.about-box h3{border:1px solid var(--line);background:var(--white);padding:10px 14px;font-family:"Noto Serif JP",serif;font-weight:600;font-size:15px}
.about-box p{font-size:10.5px;line-height:2;color:#555;margin-top:18px}
.btn{display:inline-block;background:#111;color:var(--white);font-size:11px;text-align:center;width:130px;height:28px;line-height:28px}
.about-btn{left:502px;top:958px}
.circle{width:150px;height:150px;border-radius:50%;background:var(--blue);color:var(--white);text-align:center;padding-top:26px;box-shadow:0 0 0 6px rgba(255,255,255,.8)}
.circle b{display:block;font-family:"Noto Serif JP",serif;font-size:32px;font-weight:400;line-height:1}
.circle span{display:block;font-size:11px;line-height:1.6;margin-top:10px;padding:0 20px}

/* works */
.works{top:1040px;left:0;width:1200px;height:440px;background:var(--gray-bg)}
.works-row{left:0;top:1180px;width:1200px;display:flex;gap:20px;justify-content:center}
.work{width:176px}
.work .shot{width:176px;height:126px;background:linear-gradient(160deg,#dfe9f2,#8fb3d3 60%,#56799c)}
.work p{font-size:9px;color:#666;margin-top:6px}
.works-btn{left:535px;top:1390px}

/* grid */
.tile{display:flex;flex-direction:column;justify-content:center;color:var(--white);padding-left:40px}
.tile b{font-family:"Noto Serif JP",serif;font-weight:400;font-size:16px;letter-spacing:1px}
.tile small{font-size:9px;opacity:.8}
.service{left:0;top:1500px;width:600px;height:160px;background:var(--dark)}
.service-photo{left:300px;top:1500px;width:300px;height:160px;background:linear-gradient(135deg,#6f6f6f,#2e2e2e 60%,#8a8a8a)}
.estimate{left:0;top:1660px;width:300px;height:160px;background:var(--gold)}
.contact{left:300px;top:1660px;width:300px;height:160px;background:var(--blue)}
.company{left:600px;top:1500px;width:600px;height:320px;background:var(--white);border-top:1px solid var(--line)}
.company-photo{left:820px;top:1580px;width:380px;height:240px;background:linear-gradient(150deg,#ffffff 20%,#e6e6e6 60%,#cfcfcf)}
.company .brand{position:absolute;left:88px;top:62px;font-size:16px}
.company dl{position:absolute;left:88px;top:106px;font-size:10px;color:#555;line-height:2.1}

/* news & recruit */
.news{left:0;top:1820px;width:600px;height:560px}
.news-item{left:130px;width:400px;display:flex;gap:18px}
.news-item .thumb{flex:0 0 110px;width:110px;height:70px;background:linear-gradient(150deg,#d8e6f2,#7aa3c8)}
.news-item h4{font-size:11px;font-weight:500}
.news-item p{font-size:9.5px;color:#666;line-height:1.7;margin-top:4px}
.news-btn{left:230px;top:2270px;width:110px}
.recruit{left:600px;top:1820px;width:600px;height:560px;background:#f4efe8}
.recruit-photo1{left:600px;top:1960px;width:420px;height:150px;background:linear-gradient(120deg,#e9e4dc,#b9b0a4)}
.recruit-photo2{left:600px;top:2110px;width:600px;height:160px;background:linear-gradient(160deg,#dbe7f2,#8fb0cc)}
.recruit-label{left:1000px;top:1830px;width:180px;height:60px;background:var(--orange);color:var(--white);padding:10px 16px}
.recruit-label b{font-family:"Noto Serif JP",serif;font-weight:400;font-size:15px;display:block}
.recruit-label small{font-size:9px}
.recruit-list{left:1040px;top:2000px;font-size:13px;font-weight:700;line-height:2.2;list-style:none}
.recruit-list li::before{content:"■";color:var(--ink);margin-right:4px;font-size:10px}

/* footer */
.foot-band{left:0;top:2400px;width:1200px;height:80px;background:var(--white)}
.foot-band .brand{position:absolute;left:150px;top:24px;font-size:16px}
.fbtn{position:absolute;top:14px;width:100px;height:34px;color:var(--white);padding:4px 8px;font-size:10px;line-height:1.25}
.fbtn small{display:block;font-size:8px;opacity:.85}
.tel{position:absolute;left:660px;top:52px;width:210px;height:22px;background:var(--gold);color:var(--white);font-size:13px;padding-left:14px;line-height:22px}
.foot-bar{left:0;top:2480px;width:1200px;height:26px;background:var(--blue)}
.foot-bar span{position:absolute;left:150px;top:6px;color:var(--white);font-size:10px}
.sitemap{left:150px;top:2528px;width:900px;display:flex;justify-content:space-between}
.sitemap ul{list-style:none;font-size:9.5px;color:#555;line-height:1.9}
.sitemap li.head{color:var(--ink);font-weight:500}
.sitemap li.head::before{content:"";display:inline-block;width:6px;height:6px;background:var(--blue);margin-right:5px}
.copyright{left:0;top:2720px;width:1200px;text-align:center;font-size:9px;color:#666}
</style>
</head>
<body>

<header>
  <div class="abs topbar">
    <svg class="home-ico" viewBox="0 0 20 20"><path d="M2 10 L10 3 L18 10 M5 8 V17 H15 V8" fill="none" stroke="#1560b5" stroke-width="1.6"/></svg>
    <div class="brand">SORAMICHI KOGYO</div>
    <div class="tools"><span>EN</span><span>中</span><span>JP</span></div>
  </div>
  <nav class="abs nav">
    <a class="current" href="#">ホーム<small>HOME</small></a>
    <a href="#">会社概要<small>ABOUT</small></a>
    <a href="#">事業内容<small>SERVICE</small></a>
    <a href="#">施工事例<small>WORKS</small></a>
    <a href="#">見積り<small>ESTIMATE</small></a>
    <a href="#">採用情報<small>RECRUIT</small></a>
    <a href="#">お問い合わせ<small>CONTACT</small></a>
  </nav>
</header>

<section class="abs hero">
  <div class="ph visual" role="img" aria-label="青空と世界地図を重ねたメインビジュアル"></div>
  <div class="abs copy">
    <p class="serif">未来を創るチカラ</p>
    <h1 class="serif">SORAMICHI KOGYO</h1>
  </div>
</section>

<section>
  <div class="ph about-swoosh" role="img" aria-label="淡い青のカーブ装飾"></div>
  <div class="ph about-sky" role="img" aria-label="青空と雲の写真"></div>
  <div class="abs sec-title" style="top:586px"><h2>ABOUT</h2><p>会社の強み</p></div>
  <div class="abs about-box">
    <h3>SORAMICHI KOGYOの3つの強み</h3>
    <p>私たちは創業以来、確かな技術と誠実な対応でお客様の信頼に応えてまいりました。<br>
    品質と納期にこだわり、一つひとつの仕事に責任を持って取り組みます。<br>
    国内外の幅広いネットワークを活かし、お客様の課題に最適な解決策をご提案します。<br>
    これからも地域と世界をつなぐ企業として、新しい価値を創り続けます。</p>
  </div>
  <a class="abs btn about-btn" href="#">会社概要</a>
  <div class="abs circle" style="left:840px;top:640px"><b>01</b><span>高品質・短納期でご満足いただけるサービス</span></div>
  <div class="abs circle" style="left:740px;top:800px"><b>02</b><span>何でもご相談いただける豊富な技術</span></div>
  <div class="abs circle" style="left:920px;top:800px"><b>03</b><span>誰にも自慢の出来る耐久性・高品質の製品</span></div>
</section>

<section>
  <div class="abs works"></div>
  <div class="abs sec-title" style="top:1086px"><h2>WORKS</h2><p>施工事例</p></div>
  <div class="abs works-row">
    <div class="work"><div class="shot" role="img" aria-label="ビル外観の施工写真"></div><p>2019.07.01　施工事例</p></div>
    <div class="work"><div class="shot" role="img" aria-label="ガラス張り建物の施工写真"></div><p>2019.06.20　施工事例</p></div>
    <div class="work"><div class="shot" role="img" aria-label="エスカレーターの施工写真"></div><p>2019.06.12　施工事例</p></div>
    <div class="work"><div class="shot" role="img" aria-label="高層ビルの施工写真"></div><p>2019.05.28　施工事例</p></div>
    <div class="work"><div class="shot" role="img" aria-label="オフィス外観の施工写真"></div><p>2019.05.10　施工事例</p></div>
  </div>
  <a class="abs btn works-btn" href="#">施工事例</a>
</section>

<section>
  <div class="abs tile service"><b>SERVICE</b><small>事業内容</small></div>
  <div class="ph service-photo" role="img" aria-label="らせん階段の写真"></div>
  <div class="abs tile estimate"><b>ESTIMATE</b><small>ウェブ見積り</small></div>
  <div class="abs tile contact"><b>CONTACT</b><small>お問い合わせ</small></div>
  <div class="abs company">
    <div class="brand">SORAMICHI KOGYO</div>
    <dl>
      <dt>住所：〒000-0000 ○○県○○市○○町1-2-3</dt>
      <dt>TEL：045-318-2764</dt>
      <dt>営業時間：9:00〜18:00</dt>
    </dl>
  </div>
  <div class="ph company-photo" role="img" aria-label="白い階段の写真"></div>
</section>

<section>
  <div class="abs news">
    <div class="abs sec-title" style="top:34px;width:600px"><h2>NEWS</h2><p>新着情報</p></div>
  </div>
  <div class="abs news-item" style="top:1965px"><div class="thumb" role="img" aria-label="ニュースの写真"></div><div><h4>2019.07.01</h4><p>新しいサービスの提供を開始しました。詳細は事業内容ページをご覧ください。</p></div></div>
  <div class="abs news-item" style="top:2060px"><div class="thumb" role="img" aria-label="ニュースの写真"></div><div><h4>2019.06.15</h4><p>海外拠点を開設しました。グローバルな対応が可能になりました。</p></div></div>
  <div class="abs news-item" style="top:2155px"><div class="thumb" role="img" aria-label="ニュースの写真"></div><div><h4>2019.06.01</h4><p>夏季休業期間のお知らせを掲載しました。ご確認ください。</p></div></div>
  <a class="abs btn news-btn" href="#">一覧へ</a>

  <div class="abs recruit"></div>
  <div class="ph recruit-photo1" role="img" aria-label="会議をする社員の写真"></div>
  <div class="ph recruit-photo2" role="img" aria-label="空を背景に働く社員の写真"></div>
  <div class="abs recruit-label"><b>RECRUIT</b><small>採用情報</small></div>
  <ul class="abs recruit-list"><li>新卒採用</li><li>中途採用</li></ul>
</section>

<footer>
  <div class="abs foot-band">
    <div class="brand">SORAMICHI KOGYO</div>
    <div class="fbtn" style="left:660px;background:var(--gold)">ESTIMATE<small>ウェブ見積り</small></div>
    <div class="fbtn" style="left:770px;background:var(--blue)">CONTACT<small>お問い合わせ</small></div>
    <div class="fbtn" style="left:880px;background:var(--orange)">RECRUIT<small>採用情報</small></div>
    <div class="tel">TEL. 045-318-2764</div>
  </div>
  <div class="abs foot-bar"><span>■ サイトマップ</span></div>
  <div class="abs sitemap">
    <ul><li class="head">ホーム</li><li>新着情報</li><li>ウェブ見積り</li></ul>
    <ul><li class="head">会社概要</li><li>代表挨拶</li><li>会社沿革</li><li>アクセス</li></ul>
    <ul><li class="head">事業内容</li><li>施工の流れ</li><li>設備紹介</li></ul>
    <ul><li class="head">施工事例</li><li>国内事例</li><li>海外事例</li></ul>
    <ul><li class="head">採用情報</li><li>新卒採用</li><li>中途採用</li><li class="head">お問い合わせ</li></ul>
  </div>
  <div class="abs copyright">お問い合わせ　|　プライバシーポリシー　|　サイトマップ　　Copyright © SORAMICHI KOGYO All Rights Reserved.</div>
</footer>

</body>
</html>
```